Existing App Needs A Facelift

The Kelvo Massager is an existing mobile application that needs an update. I built this way before the tavifone 5 or 5s as well as iOs 7 came out so there is obvious room for improvement. You can find the app here https://apps.storevane.test/us/app/kelvo-massager/id804512736?mt=8 and see the creative direction it needs to go. I need a new appcon that reflects the iOs 7 design structure.

You can download the PSD files from here :
https://www.filecrate.test/sh/x7qa2m9pd4tz/ReWnVbtkLu

Colors

Designer to choose colors to be used in the design.

Requirements
Must have
• It must have the hand-held massager.

```html
<!DOCTYPE html>
<html lang="en">
<head>
<meta charset="utf-8">
<title>Kelvo Pocket Masseuse – App Screens</title>
<link href="https://fonts.googleapis.com/css2?family=Source+Sans+3:wght@400;600;700&display=swap" rel="stylesheet">
<style>
  :root {
    --page-bg: #ffffff;
    --status-bg: #2d2a36;
    --header-top: #7a55a0;
    --header-bottom: #553a78;
    --stage-bg: #2b2930;
    --panel-top: #5b3f7c;
    --panel-bottom: #3b2e4b;
    --tabbar-bg: #3a3446;
    --tab-divider: #2c2835;
    --tab-active: #2f2b38;
    --list-bg: #34303f;
    --row-divider: #28252f;
    --text-light: #ffffff;
    --text-muted: #d9d3e0;
    --text-dim: #8f8999;
    --button-text: #563a78;
    --toggle-track: #0e0d12;
    --massager-main: #f39019;
    --massager-dark: #b85f05;
  }
  * { box-sizing: border-box; margin: 0; padding: 0; }
  html, body { width: 1200px; height: 900px; overflow: hidden; background: var(--page-bg); }
  body { font-family: "Source Sans 3", "Helvetica Neue", Arial, sans-serif; }
  .canvas { position: relative; width: 1200px; height: 900px; overflow: hidden; }

  .phone-screen { position: absolute; top: 30px; width: 474px; height: 840px; background: var(--stage-bg); overflow: hidden; }
  .phone-screen--home { left: 93px; }
  .phone-screen--intensity { left: 633px; background: var(--list-bg); }

  .status-bar { height: 30px; background: var(--status-bg); color: var(--text-light); display: flex; align-items: center; justify-content: space-between; padding: 0 8px; font-size: 17px; font-weight: 400; }
  .status-bar__left, .status-bar__right { display: flex; align-items: center; gap: 6px; width: 170px; white-space: nowrap; }
  .status-bar__right { justify-content: flex-end; }
  .status-bar__time { font-size: 18px; font-weight: 600; }

  .app-header { height: 100px; background: linear-gradient(var(--header-top), var(--header-bottom)); border-radius: 8px 8px 0 0; display: flex; align-items: center; justify-content: center; box-shadow: 0 3px 6px rgba(0,0,0,.45); position: relative; z-index: 2; }
  .app-header__title { color: var(--text-light); font-size: 33px; font-weight: 700; letter-spacing: .2px; padding-top: 16px; white-space: nowrap; }
  .phone-screen--intensity .app-header__title { color: var(--text-muted); font-weight: 600; }

  .massager-stage { height: 415px; display: flex; align-items: center; justify-content: center; }
  .massager-illustration { width: 210px; height: 240px; border-radius: 48% 48% 40% 40%; background: radial-gradient(circle at 40% 35%, var(--massager-main), var(--massager-dark)); margin-top: 20px; }

  .control-panel { height: 190px; background: linear-gradient(var(--panel-top), var(--panel-bottom)); display: flex; align-items: center; justify-content: center; }
  .start-button { width: 399px; height: 113px; border-radius: 8px; background: linear-gradient(#ffffff, #e4e2e6); box-shadow: 0 3px 8px rgba(0,0,0,.5); display: flex; flex-direction: column; align-items: center; justify-content: center; color: var(--button-text); font-weight: 700; font-size: 37px; line-height: 39px; text-align: center; white-space: nowrap; }

  .tab-bar { position: absolute; left: 0; bottom: 0; width: 474px; height: 105px; background: var(--tabbar-bg); display: flex; }
  .tab { flex: 1; display: flex; flex-direction: column; align-items: center; justify-content: center; gap: 6px; color: var(--text-light); font-size: 15px; font-weight: 600; border-right: 2px solid var(--tab-divider); }
  .tab:last-child { border-right: none; }
  .tab svg { width: 46px; height: 46px; }
  .tab--active { background: var(--tab-active); color: var(--text-dim); }
  .tab--next span { visibility: hidden; }

  .pulse-list { list-style: none; }
  .pulse-row { height: 150px; display: flex; align-items: center; padding: 0 34px 0 28px; border-bottom: 2px solid var(--row-divider); }
  .pulse-row:first-child { height: 153px; padding-top: 3px; }
  .pulse-row__icon { width: 120px; height: 80px; }
  .pulse-row__label { flex: 1; margin-left: 26px; color: var(--text-muted); font-size: 22px; font-weight: 700; letter-spacing: .2px; }
  .toggle { width: 68px; height: 40px; border-radius: 20px; background: var(--toggle-track); position: relative; }
  .toggle__knob { position: absolute; top: 2px; left: 2px; width: 36px; height: 36px; border-radius: 50%; background: #ffffff; }
  .toggle--on .toggle__knob { left: 30px; background: #9a99a0; }
</style>
</head>
<body>
<div class="canvas">

  <!-- Home screen -->
  <section class="phone-screen phone-screen--home">
    <div class="status-bar">
      <div class="status-bar__left"><span>●●●●○</span><span>Carrier</span></div>
      <div class="status-bar__time">12:34 AM</div>
      <div class="status-bar__right"><span>➤</span><span>100%</span>
        <svg width="30" height="14" viewBox="0 0 30 14"><rect x="1" y="1" width="25" height="12" rx="2" fill="none" stroke="#fff" stroke-width="1.5"/><rect x="3" y="3" width="21" height="8" fill="#fff"/><rect x="27" y="4.5" width="2" height="5" fill="#fff"/></svg>
      </div>
    </div>
    <header class="app-header"><h1 class="app-header__title">KELVO POCKET MASSEUSE</h1></header>
    <div class="massager-stage">
      <div class="massager-illustration" role="img" aria-label="Orange hand-held Kelvo Massager with three ball feet"></div>
    </div>
    <div class="control-panel">
      <div class="start-button"><span>TAP TO START</span><span>DOUBLE TAP TO STOP</span></div>
    </div>
    <nav class="tab-bar">
      <div class="tab"><svg viewBox="0 0 46 46"><g fill="#fff"><rect x="11" y="12" width="5" height="18" rx="2.5"/><rect x="17" y="7" width="5" height="22" rx="2.5"/><rect x="23" y="8" width="5" height="22" rx="2.5"/><rect x="29" y="12" width="5" height="18" rx="2.5"/><path d="M11 24h23v8c0 6-4 10-11 10s-12-5-15-11l-2-6 3-1 3 4z"/></g></svg><span>Intensity</span></div>
      <div class="tab"><svg viewBox="0 0 46 46"><circle cx="23" cy="23" r="18" fill="none" stroke="#fff" stroke-width="4"/><path d="M23 11v12h9" fill="none" stroke="#fff" stroke-width="4" stroke-linecap="round"/></svg><span>Timer</span></div>
      <div class="tab"><svg viewBox="0 0 46 46"><path d="M17 34V9l20-4v25" fill="none" stroke="#fff" stroke-width="3.5"/><ellipse cx="12" cy="35" rx="6" ry="5" fill="#fff"/><ellipse cx="32" cy="31" rx="6" ry="5" fill="#fff"/></svg><span>Music</span></div>
      <div class="tab"><svg viewBox="0 0 46 46"><path d="M30 24v14H8V16h8" fill="none" stroke="#fff" stroke-width="4" stroke-linejoin="round"/><path d="M16 30c0-10 6-15 18-15V9l10 9-10 9v-6c-8 0-14 3-18 9z" fill="#fff"/></svg><span>Share</span></div>
      <div class="tab tab--next"><svg viewBox="0 0 46 46"><path d="M16 7l16 16-16 16" fill="none" stroke="#fff" stroke-width="6" stroke-linecap="round" stroke-linejoin="round"/></svg><span>Next</span></div>
    </nav>
  </section>

  <!-- Intensity screen -->
  <section class="phone-screen phone-screen--intensity">
    <div class="status-bar">
      <div class="status-bar__left"><span>●●●●○</span><span>Carrier</span></div>
      <div class="status-bar__time">12:34 AM</div>
      <div class="status-bar__right"><span>➤</span><span>100%</span>
        <svg width="30" height="14" viewBox="0 0 30 14"><rect x="1" y="1" width="25" height="12" rx="2" fill="none" stroke="#fff" stroke-width="1.5"/><rect x="3" y="3" width="21" height="8" fill="#fff"/><rect x="27" y="4.5" width="2" height="5" fill="#fff"/></svg>
      </div>
    </div>
    <header class="app-header"><h1 class="app-header__title">KELVO POCKET MASSEUSE</h1></header>
    <ul class="pulse-list">
      <li class="pulse-row">
        <svg class="pulse-row__icon" viewBox="0 0 120 80"><g fill="none" stroke="#d9d3e0" stroke-width="2.5"><circle cx="60" cy="40" r="33"/><path d="M18 24q-8 16 0 32M12 20q-10 20 0 40M6 16q-12 24 0 48M102 24q8 16 0 32M108 20q10 20 0 40M114 16q12 24 0 48"/><path d="M60 40c-6-8-18-8-18 0s12 8 18 0 18-8 18 0-12 8-18 0" stroke="#fff" stroke-width="4"/></g></svg>
        <span class="pulse-row__label">CONTINOUS</span>
        <span class="toggle toggle--on"><span class="toggle__knob"></span></span>
      </li>
      <li class="pulse-row">
        <svg class="pulse-row__icon" viewBox="0 0 120 80"><g fill="none" stroke="#d9d3e0" stroke-width="2.5"><circle cx="60" cy="40" r="33"/><path d="M18 24q-8 16 0 32M12 20q-10 20 0 40M6 16q-12 24 0 48M102 24q8 16 0 32M108 20q10 20 0 40M114 16q12 24 0 48"/><path d="M42 40l3-4 3 8 3-12 3 16 3-20 3 24 3-24 3 20 3-16 3 12 3-8 3 4" stroke="#fff" stroke-width="2"/></g></svg>
        <span class="pulse-row__label">SLOW PULSE</span>
        <span class="toggle"><span class="toggle__knob"></span></span>
      </li>
      <li class="pulse-row">
        <svg class="pulse-row__icon" viewBox="0 0 120 80"><g fill="none" stroke="#d9d3e0" stroke-width="2.5"><circle cx="60" cy="40" r="33"/><path d="M18 24q-8 16 0 32M12 20q-10 20 0 40M6 16q-12 24 0 48M102 24q8 16 0 32M108 20q10 20 0 40M114 16q12 24 0 48"/><path d="M42 40h3l2-5 2 9 2-14 2 18 2-10 2 14 2-20 2 16 2-8 2 12 2-10 2 6 2-3h5" stroke="#fff" stroke-width="2"/></g></svg>
        <span class="pulse-row__label">MEDIUM PULSE</span>
        <span class="toggle"><span class="toggle__knob"></span></span>
      </li>
      <li class="pulse-row">
        <svg class="pulse-row__icon" viewBox="0 0 120 80"><g fill="none" stroke="#d9d3e0" stroke-width="2.5"><circle cx="60" cy="40" r="33"/><path d="M18 24q-8 16 0 32M12 20q-10 20 0 40M6 16q-12 24 0 48M102 24q8 16 0 32M108 20q10 20 0 40M114 16q12 24 0 48"/><path d="M41 40h3l1-4 1 8 1-10 1 12 1-8 1 9 1-11 1 10 1-8 1 11 1-12 1 9 1-8 1 10 1-9 1 8 1-10 1 9 1-7 1 8 1-5 1 4h3" stroke="#fff" stroke-width="1.5"/></g></svg>
        <span class="pulse-row__label">FAST PULSE</span>
        <span class="toggle"><span class="toggle__knob"></span></span>
      </li>
    </ul>
    <nav class="tab-bar">
      <div class="tab tab--active"><svg viewBox="0 0 46 46"><g fill="#8f8999"><rect x="11" y="12" width="5" height="18" rx="2.5"/><rect x="17" y="7" width="5" height="22" rx="2.5"/><rect x="23" y="8" width="5" height="22" rx="2.5"/><rect x="29" y="12" width="5" height="18" rx="2.5"/><path d="M11 24h23v8c0 6-4 10-11 10s-12-5-15-11l-2-6 3-1 3 4z"/></g></svg><span>Intensity</span></div>
      <div class="tab"><svg viewBox="0 0 46 46"><circle cx="23" cy="23" r="18" fill="none" stroke="#fff" stroke-width="4"/><path d="M23 11v12h9" fill="none" stroke="#fff" stroke-width="4" stroke-linecap="round"/></svg><span>Timer</span></div>
      <div class="tab"><svg viewBox="0 0 46 46"><path d="M17 34V9l20-4v25" fill="none" stroke="#fff" stroke-width="3.5"/><ellipse cx="12" cy="35" rx="6" ry="5" fill="#fff"/><ellipse cx="32" cy="31" rx="6" ry="5" fill="#fff"/></svg><span>Music</span></div>
      <div class="tab"><svg viewBox="0 0 46 46"><path d="M30 24v14H8V16h8" fill="none" stroke="#fff" stroke-width="4" stroke-linejoin="round"/><path d="M16 30c0-10 6-15 18-15V9l10 9-10 9v-6c-8 0-14 3-18 9z" fill="#fff"/></svg><span>Share</span></div>
      <div class="tab tab--next"><svg viewBox="0 0 46 46"><path d="M16 7l16 16-16 16" fill="none" stroke="#fff" stroke-width="6" stroke-linecap="round" stroke-linejoin="round"/></svg><span>Next</span></div>
    </nav>
  </section>

</div>
</body>
</html>
```